Business Card Design

Hoping for a black background business card, minimalistic design.
With the Marble Crest logo you created in white.

I would like to include:
My Name and title
Address (street address)
Reception: (phone number)
Fax: (fax number)
Reception: (email address)
Direct email: (email address)
Instagram: (ig handle)

```html
<!DOCTYPE html>
<html lang="en">
<head>
<meta charset="UTF-8">
<title>Marble Crest Business Card</title>
<link rel="stylesheet" href="https://fonts.googleapis.com/css2?family=Montserrat:wght@400;500;600;700&display=swap">
<style>
  :root {
    --canvas: #f2f2f2;
    --card: #000000;
    --ink: #ffffff;
    --ink-muted: #cfcfcf;
    --rule: #6a6a6a;
    --pattern-dark: #0b0b0b;
    --pattern-light: #1c1c1c;
  }
  * { margin: 0; padding: 0; box-sizing: border-box; }
  html, body {
    width: 1200px;
    height: 1200px;
    overflow: hidden;
    background: var(--canvas);
    font-family: "Montserrat", sans-serif;
  }
  .sheet {
    position: relative;
    width: 1200px;
    height: 1200px;
  }
  .card {
    position: absolute;
    top: 445px;
    width: 534px;
    height: 310px;
    background: var(--card);
    color: var(--ink);
    box-shadow: 0 18px 30px rgba(0,0,0,0.18);
    overflow: hidden;
  }
  .card-front { left: 43px; }
  .card-back { left: 622px; }

  .front-pattern {
    position: absolute;
    inset: 0;
    background: radial-gradient(ellipse at 30% 30%, var(--pattern-light), var(--pattern-dark) 75%);
  }
  .front-mark {
    position: absolute;
    right: 26px;
    bottom: 28px;
    display: flex;
    align-items: center;
    gap: 9px;
  }
  .mark-dot {
    width: 26px;
    height: 26px;
    border: 2px solid var(--ink);
    border-radius: 50%;
  }
  .mark-name {
    font-weight: 600;
    font-size: 13px;
    letter-spacing: 1.5px;
    text-transform: uppercase;
    color: var(--ink);
    white-space: nowrap;
  }

  .back-brand {
    position: absolute;
    top: 40px;
    right: 48px;
    display: flex;
    align-items: center;
    gap: 10px;
  }
  .back-brand .mark-dot { width: 30px; height: 30px; }
  .back-brand .brand-divider {
    width: 1px;
    height: 30px;
    background: var(--ink);
  }
  .back-brand .mark-name { font-size: 14px; letter-spacing: 1.8px; font-weight: 500; }

  .holder {
    position: absolute;
    top: 176px;
    left: 366px;
    white-space: nowrap;
  }
  .holder-name {
    font-weight: 700;
    font-size: 19px;
    letter-spacing: 0.5px;
    text-transform: uppercase;
    line-height: 22px;
  }
  .holder-title {
    font-size: 11px;
    color: var(--ink-muted);
    line-height: 14px;
  }
  .back-rule {
    position: absolute;
    top: 205px;
    left: 24px;
    width: 330px;
    height: 1px;
    background: var(--rule);
  }

  .contacts {
    position: absolute;
    left: 24px;
    top: 222px;
    font-size: 8.5px;
    line-height: 19px;
  }
  .contact-row { display: flex; gap: 28px; }
  .contact-item { white-space: nowrap; }
  .contact-label {
    font-weight: 700;
    font-size: 7px;
    letter-spacing: 0.4px;
    text-transform: uppercase;
    margin-right: 4px;
  }
</style>
</head>
<body>
<main class="sheet">

  <section class="card card-front">
    <div class="front-pattern" role="img" aria-label="Tone-on-tone repeating brand pattern across the card face"></div>
    <div class="front-mark">
      <span class="mark-dot"></span>
      <span class="mark-name">Marble Crest</span>
    </div>
  </section>

  <section class="card card-back">
    <div class="back-brand">
      <span class="mark-dot"></span>
      <span class="brand-divider"></span>
      <span class="mark-name">Marble Crest</span>
    </div>

    <div class="holder">
      <p class="holder-name">Daniel Reyes</p>
      <p class="holder-title">Marketing Director</p>
    </div>

    <div class="back-rule"></div>

    <div class="contacts">
      <div class="contact-row">
        <span class="contact-item"><span class="contact-label">Reception :</span>+(555)010-2834</span>
        <span class="contact-item"><span class="contact-label">Fax :</span>+(555)010-2835</span>
      </div>
      <div class="contact-row">
        <span class="contact-item"><span class="contact-label">Direct :</span>hello@marblecrest.com</span>
        <span class="contact-item"><span class="contact-label">Reception :</span>hello@marblecrest.com</span>
      </div>
      <div class="contact-row">
        <span class="contact-item"><span class="contact-label">Address :</span>48 Harbor Lane Westfield, Oregon, USA, 97201</span>
      </div>
    </div>
  </section>

</main>
</body>
</html>
```